I am an accountant and I am interested in publicising workshops, seminars and networking events. I have included some publicity materials produced by my franchise company which can be used as a basis for the design.

Side 1: should show the basic design. I need my contact details to be included as follows: Jenna Pricott, Lumbrell Accounting, 47 Harcombe Street, Fennwick Row, EC1V 8QN. Tel: 07412 637208. Email: jennapricott@lumbrell.example
www.lumbrellnorthside.example

Side 2: can use elements of the basic design submitted or parts of the franchise website for www.lumbrell.example. This side should lead people to my workshops. These are detailed here on this website www.lumbrell.example. (seminars top menu) At the moment there are four seminars, so they should not go into detail about any specific seminar as they may change in the future. I also have a free ebook so I also want this mentioned in the text.

```html
<!DOCTYPE html>
<html lang="en">
<head>
<meta charset="utf-8">
<title>Networking Events &amp; Workshops</title>
<link rel="stylesheet" href="https://fonts.googleapis.com/css2?family=Bitter:wght@700&family=Open+Sans:wght@400;700&display=swap">
<style>
  :root {
    --orange: #f3a31f;
    --heading: #e8921a;
    --ink: #3a3a3a;
    --band: #2e3b4b;
    --white: #ffffff;
    --photo-light: #eef2f6;
    --photo-mid: #b9c4cf;
  }
  * { margin: 0; padding: 0; box-sizing: border-box; }
  html, body { width: 847px; height: 1200px; overflow: hidden; background: var(--white); }
  .flyer {
    position: relative; width: 847px; height: 1200px; overflow: hidden;
    background: var(--white);
    font-family: "Open Sans", Arial, sans-serif; color: var(--ink);
  }
  .hero-photo {
    position: absolute; left: 0; top: 0; width: 847px; height: 270px;
    background: linear-gradient(180deg, var(--photo-mid) 0%, var(--photo-light) 70%, var(--white) 100%);
  }
  .title-banner {
    position: absolute; left: 34px; top: 113px; width: 404px; height: 142px;
    background: var(--orange);
    display: flex; align-items: center; padding: 0 26px;
  }
  .title-banner h1 {
    font-family: "Bitter", Georgia, serif; font-weight: 700;
    color: var(--white); font-size: 36px; line-height: 1.2;
  }
  .columns {
    position: absolute; top: 272px; left: 34px; width: 786px;
    display: grid; grid-template-columns: 381px 368px; column-gap: 37px;
  }
  .event { margin-bottom: 30px; }
  .event h2 {
    color: var(--heading); font-weight: 700; font-size: 20px; line-height: 1.25;
    margin-bottom: 12px;
  }
  .event p { font-size: 14.5px; line-height: 1.42; margin-bottom: 14px; }
  .event .link { margin-bottom: 0; }
  .event strong { font-weight: 700; }
  .contact-list { list-style: none; font-size: 14.5px; line-height: 1.42; }
  .right-col { padding-top: 18px; }
  .footer-band {
    position: absolute; left: 0; bottom: 0; width: 847px; height: 133px;
    background: var(--band); color: var(--white);
    display: flex; flex-direction: column; justify-content: center; align-items: center;
    text-align: center; font-size: 17px; line-height: 1.45;
  }
  .footer-band strong { font-weight: 700; }
</style>
</head>
<body>
<div class="flyer">
  <div class="hero-photo" role="img" aria-label="Business people meeting in a bright office"></div>
  <div class="title-banner"><h1>Networking Events<br>&amp; Workshops</h1></div>

  <div class="columns">
    <div class="left-col">
      <section class="event">
        <h2>Lumbrell Workshops &amp; Seminars</h2>
        <p>Whether you have a business idea or already run your own company, our workshops and seminars give you practical guidance from experienced accountants. Sessions cover the topics that matter most to growing businesses, from getting started and planning ahead to keeping your finances healthy and your business profitable.</p>
        <p class="link">To see the seminars currently on offer and book your place, visit the seminars page at<br><strong>www.lumbrell.example</strong></p>
      </section>
      <section class="event">
        <h2>Free Business Ebook</h2>
        <p>Looking for straightforward advice you can read at your own pace? Our free ebook is packed with useful tips to help you run your business with confidence, plan your cash flow and make smarter decisions for the future.</p>
        <p class="link">To download your free copy, visit<br><strong>www.lumbrellnorthside.example</strong></p>
      </section>
    </div>
    <div class="right-col">
      <section class="event">
        <h2>Networking Events</h2>
        <p>Imagine making more contacts in one hour than some people do in a career. Our networking events bring together business owners from a wide range of sectors and industries, giving you the perfect place to share ideas, build relationships and grow your book of contacts.</p>
        <p class="link">For upcoming dates, visit<br><strong>www.lumbrellnorthside.example</strong></p>
      </section>
      <section class="event">
        <h2>Get In Touch</h2>
        <ul class="contact-list">
          <li><strong>Jenna Pricott</strong></li>
          <li>Lumbrell Accounting</li>
          <li>47 Harcombe Street</li>
          <li>Fennwick Row</li>
          <li>EC1V 8QN</li>
          <li>Tel: 07412 637208</li>
          <li>Email: jennapricott@lumbrell.example</li>
          <li>www.lumbrellnorthside.example</li>
        </ul>
      </section>
    </div>
  </div>

  <footer class="footer-band">
    <p>We have many more events which you might find useful. For further information</p>
    <p>check out our website <strong>www.lumbrellnorthside.example</strong></p>
    <p>To download a free ebook to help you run your business,</p>
    <p>check our website <strong>www.lumbrellnorthside.example</strong></p>
  </footer>
</div>
</body>
</html>
```